New Graphic Design Project

Design a simple and clean PowerPoint slide templates for a Board meeting. The slides should have predominantly white backgrounds and use the brand graphic standards (attached). I'm also attached a PowerPoint master that I don't like, as it's too basic.
The company name is Harbor Lane Gauging.
It sells, calibrates, services and repairs industrial and commercial scales of all types. In particular, Truck scales, floor scales, counting scales and benchtop scales.
The website is harborlanegauging.example but this are the old colors, so ignore the logo and colors. We are launching a new logo and new look. Several variations of the logo are available.

```html
<!DOCTYPE html>
<html lang="en">
<head>
<meta charset="utf-8">
<title>Harbor Lane Gauging — Board Meeting Slide Templates</title>
<link href="https://fonts.googleapis.com/css2?family=Archivo:wght@400;500;600;700&family=Russo+One&display=swap" rel="stylesheet">
<style>
  :root{
    --navy:#1c315e;
    --orange:#f7931e;
    --canvas:#e6e7e9;
    --white:#ffffff;
    --ink:#4a4f5c;
    --rule:#d6d9df;
    --caption:#8b8d91;
    --display:"Russo One", sans-serif;
    --body:"Archivo", sans-serif;
  }
  *{margin:0;padding:0;box-sizing:border-box}
  html,body{width:1200px;height:810px;overflow:hidden}
  body{background:var(--canvas);position:relative;font-family:var(--body);color:var(--ink)}

  .slide{position:absolute;width:293px;height:165px;overflow:hidden;
    box-shadow:0 10px 22px rgba(20,30,60,.18),0 2px 5px rgba(20,30,60,.08)}
  .slide--light{background:var(--white)}
  .slide--dark{background:var(--navy)}

  /* company name block */
  .wordmark{position:absolute;display:flex;align-items:center;gap:2.5px;
    font-family:var(--display);font-size:5px;letter-spacing:.35px;line-height:1.02;white-space:nowrap}
  .wordmark i{display:block;width:6px;height:6px;background:var(--orange);flex:none}
  .wordmark--light{color:var(--white)}
  .wordmark--dark{color:var(--navy)}

  .url{position:absolute;font-size:3.6px;line-height:1.3;white-space:nowrap}
  .slide--light .url{color:#7b7f88}
  .slide--dark .url{color:#c9d0de}

  /* cover */
  .cover-photo{position:absolute;inset:0;
    background:radial-gradient(ellipse at 72% 40%,#2f4676 0%,#1f3362 45%,#15264b 100%)}
  .cover-title{position:absolute;left:0;right:0;top:63px;text-align:center;
    font-family:var(--display);font-size:16.5px;color:var(--white);letter-spacing:.2px;font-weight:400}
  .cover-rule{position:absolute;left:92px;width:109px;top:85px;height:.7px;background:var(--orange)}
  .cover-company{position:absolute;left:0;right:0;top:91px;text-align:center;
    font-size:6.4px;letter-spacing:1.6px;color:var(--white)}
  .cover-meta{position:absolute;left:0;right:0;top:140px;text-align:center;
    font-size:3.9px;font-weight:600;color:var(--orange)}
  .cover-meta span{color:#c9d0de;margin:0 3px}
  .chevron{position:absolute;left:143px;top:20px}

  /* agenda */
  .agenda-band{position:absolute;left:0;top:0;bottom:0;width:59px;background:var(--navy)}
  .agenda-word{position:absolute;left:29.5px;top:82px;transform:translate(-50%,-50%) rotate(-90deg);
    font-family:var(--display);font-size:18px;color:var(--orange);letter-spacing:.4px}
  .title-bar{position:absolute;width:.8px;background:var(--orange)}
  .slide-title{position:absolute;font-family:var(--display);color:var(--navy);white-space:nowrap;font-weight:400}
  .slide-sub{position:absolute;font-size:3.6px;font-weight:600;color:#6b7080;text-transform:uppercase;white-space:nowrap}
  .agenda-item{position:absolute;left:77px;width:201px;height:24px}
  .agenda-num{position:absolute;left:0;top:0;font-size:6.4px;font-weight:600;color:var(--orange)}
  .agenda-head{position:absolute;left:28px;top:0;font-size:6.2px;font-weight:600;color:var(--navy)}
  .agenda-desc{position:absolute;left:28px;top:8px;font-size:3.5px;color:#7b7f88;white-space:nowrap}
  .agenda-rule{position:absolute;left:77px;width:201px;height:.5px;background:var(--rule)}

  /* section divider */
  .crumb{position:absolute;left:16px;top:20px;font-size:3.4px;font-weight:600;color:#d9dfea;white-space:nowrap}
  .section-num{position:absolute;right:16px;top:35px;font-family:var(--display);font-size:60px;
    line-height:1;color:var(--orange);letter-spacing:-1px}
  .section-name{position:absolute;right:16px;top:95px;font-size:12.6px;font-weight:600;color:var(--white);white-space:nowrap}
  .section-rule{position:absolute;right:16px;top:116px;width:52px;height:.7px;background:var(--orange)}

  /* two-column content */
  .col{position:absolute;width:122px}
  .col-head{font-size:6.8px;font-weight:500;color:var(--navy);line-height:1.1}
  .col-head b{color:var(--orange);font-weight:700;margin-right:1px}
  .col-desc{font-size:3.6px;line-height:1.35;color:#555a66;margin-top:1px}
  .point{margin-left:4px}
  .point-head{font-size:5px;font-weight:600;color:var(--navy);line-height:1.1}
  .point-desc{font-size:3.3px;line-height:1.35;color:#555a66}

  /* text content */
  .body-copy{position:absolute;left:28px;width:243px;font-size:3.6px;line-height:1.4;color:#444955}

  /* thank you */
  .thanks{position:absolute;left:0;right:0;top:66px;text-align:center;font-size:15.6px;font-weight:700;color:var(--white)}
  .thanks-copy{position:absolute;left:0;right:0;top:86px;text-align:center;font-size:3.8px;line-height:1.6;color:#d9dfea}
  .thanks-rule{position:absolute;left:120.5px;top:103px;width:52px;height:.7px;background:var(--orange)}

  .caption{position:absolute;right:117px;top:749px;font-size:10px;font-weight:500;color:var(--caption);white-space:nowrap}
</style>
</head>
<body>

<!-- Cover -->
<section class="slide slide--dark" style="left:117px;top:110px">
  <div class="cover-photo" role="img" aria-label="Photograph of a tanker truck on an industrial road, tinted deep navy"></div>
  <div class="wordmark wordmark--light" style="left:16px;top:18px"><i></i><span>HARBOR LANE<br>GAUGING</span></div>
  <svg class="chevron" width="7" height="5" viewBox="0 0 7 5"><path d="M.6.8 3.5 3.8 6.4.8" fill="none" stroke="#f7931e" stroke-width=".8"/></svg>
  <h1 class="cover-title">BOARD MEETING</h1>
  <div class="cover-rule"></div>
  <div class="cover-company">HARBOR LANE GAUGING</div>
  <div class="cover-meta">JUNE 24, 2026<span>|</span>CORPORATE HEADQUARTERS</div>
  <div class="url" style="left:0;right:0;top:147px;text-align:center">harborlanegauging.example</div>
</section>

<!-- Agenda -->
<section class="slide slide--light" style="left:452px;top:114px">
  <div class="agenda-band"></div>
  <div class="agenda-word">AGENDA</div>
  <div class="title-bar" style="left:72px;top:15px;height:9px"></div>
  <h2 class="slide-title" style="left:77px;top:15px;font-size:7.8px">BOARD MEETING OVERVIEW</h2>
  <div class="slide-sub" style="left:77px;top:26px">HARBOR LANE GAUGING | BOARD CONFIDENTIAL</div>
  <div class="wordmark wordmark--dark" style="right:15px;top:15px"><i></i><span>HARBOR LANE<br>GAUGING</span></div>

  <div class="agenda-item" style="top:41px"><span class="agenda-num">01</span><span class="agenda-head">Opening Remarks</span><span class="agenda-desc">Lorem ipsum dolor sit amet, consectetur adipiscing elit, sed.</span></div>
  <div class="agenda-rule" style="top:59px"></div>
  <div class="agenda-item" style="top:66px"><span class="agenda-num">02</span><span class="agenda-head">Financial Review</span><span class="agenda-desc">Do eiusmod tempor incididunt ut labore et dolore magna aliqua.</span></div>
  <div class="agenda-rule" style="top:84px"></div>
  <div class="agenda-item" style="top:90px"><span class="agenda-num">03</span><span class="agenda-head">Operations update</span><span class="agenda-desc">Ut enim ad minim veniam, quis nostrud exercitation ullamco laboris.</span></div>
  <div class="agenda-rule" style="top:108px"></div>
  <div class="agenda-item" style="top:115px"><span class="agenda-num">04</span><span class="agenda-head">Strategic Priorities</span><span class="agenda-desc">Nisi ut aliquip ex ea commodo consequat duis aute irure dolor in reprehenderit.</span></div>
  <div class="agenda-rule" style="top:133px"></div>
  <div class="agenda-item" style="top:139px"><span class="agenda-num">05</span><span class="agenda-head">Decisions &amp; Next Steps</span><span class="agenda-desc">Excepteur sint occaecat cupidatat non proident, sunt in culpa.</span></div>
</section>

<!-- Section 01 -->
<section class="slide slide--dark" style="left:790px;top:116px">
  <div class="crumb">BOARD MEETING | SECTION OVERVIEW</div>
  <div class="section-num">01</div>
  <div class="section-name">OPENING REMARKS</div>
  <div class="section-rule"></div>
  <div class="wordmark wordmark--light" style="right:16px;top:142px"><i></i><span>HARBOR LANE<br>GAUGING</span></div>
</section>

<!-- Opening remarks: columns -->
<section class="slide slide--light" style="left:117px;top:324px">
  <div class="title-bar" style="left:16px;top:16px;height:9px"></div>
  <h2 class="slide-title" style="left:22px;top:16px;font-size:7.4px">OPENING REMARKS</h2>
  <div class="slide-sub" style="left:22px;top:26px">Lorem ipsum dolor sit amet, consectetur adipiscing elit, sed.</div>
  <div class="col" style="left:25px;top:43px">
    <div class="col-head"><b>•</b>Sed Ut Perspiciatis</div>
    <div class="col-desc">unde omnis iste natus error sit voluptatem accusantium doloremque laudantium, totam rem aperiam.</div>
    <div class="point" style="margin-top:9px"><div class="point-head">Nemo enim</div><div class="point-desc">Ipsam voluptatem quia voluptas sit aspernatur aut odit<br>aut fugit</div></div>
    <div class="point" style="margin-top:4px"><div class="point-head">Consequuntur</div><div class="point-desc">magni dolores eos qui ratione voluptatem sequi nesciunt.<br>Neque porro quisquam</div></div>
    <div class="point" style="margin-top:4px"><div class="point-head">Adipisci Velit</div><div class="point-desc">sed quia non numquam eius modi tempora incidunt ut labore et dolore magnam aliquam quaerat voluptatem.</div></div>
  </div>
  <div class="col" style="left:158px;top:43px">
    <div class="col-head"><b>•</b>Quis autem vel</div>
    <div class="col-desc">unde omnis iste natus error sit voluptatem accusantium doloremque laudantium, totam rem aperiam, eaque ipsa quae.</div>
    <div class="point" style="margin-top:9px"><div class="point-head">Nemo enim</div><div class="point-desc">Ipsam voluptatem quia voluptas sit aspernatur aut odit<br>aut fugit</div></div>
    <div class="point" style="margin-top:4px"><div class="point-head">Consequuntur</div><div class="point-desc">magni dolores eos qui ratione voluptatem sequi nesciunt.<br>Neque porro quisquam</div></div>
    <div class="point" style="margin-top:4px"><div class="point-head">Adipisci Velit</div><div class="point-desc">sed quia non numquam eius modi tempora incidunt ut labore et dolore magnam aliquam quaerat voluptatem.</div></div>
  </div>
  <div class="wordmark wordmark--dark" style="left:16px;top:142px"><i></i><span>HARBOR LANE<br>GAUGING</span></div>
  <div class="url" style="right:16px;top:145px">harborlanegauging.example</div>
</section>

<!-- Opening remarks: text -->
<section class="slide slide--light" style="left:452px;top:323px">
  <div class="title-bar" style="left:16px;top:16px;height:9px"></div>
  <h2 class="slide-title" style="left:22px;top:16px;font-size:7.4px">OPENING REMARKS</h2>
  <div class="slide-sub" style="left:22px;top:26px">Lorem ipsum dolor sit amet, consectetur adipiscing elit, sed.</div>
  <p class="body-copy" style="top:46px">At vero eos et accusamus et iusto odio dignissimos ducimus qui blanditiis praesentium voluptatum deleniti atque corrupti quos dolores et quas molestias excepturi sint occaecati cupiditate non provident, similique sunt in culpa qui officia deserunt mollitia animi, id est laborum et dolorum fuga.</p>
  <p class="body-copy" style="top:69px;width:215px">Et harum quidem rerum facilis est et expedita distinctio. Nam libero tempore, cum soluta nobis est eligendi optio cumque nihil impedit quo minus id quod maxime placeat facere possimus.</p>
  <div class="wordmark wordmark--dark" style="left:16px;top:142px"><i></i><span>HARBOR LANE<br>GAUGING</span></div>
  <div class="url" style="right:16px;top:145px">harborlanegauging.example</div>
</section>

<!-- Section 02 -->
<section class="slide slide--dark" style="left:790px;top:325px">
  <div class="crumb">BOARD MEETING | SECTION OVERVIEW</div>
  <div class="section-num">02</div>
  <div class="section-name">FINANCIAL REVIEW</div>
  <div class="section-rule"></div>
  <div class="wordmark wordmark--light" style="right:16px;top:142px"><i></i><span>HARBOR LANE<br>GAUGING</span></div>
</section>

<!-- Financial review: columns -->
<section class="slide slide--light" style="left:117px;top:534px">
  <div class="title-bar" style="left:16px;top:16px;height:9px"></div>
  <h2 class="slide-title" style="left:22px;top:16px;font-size:7.4px">FINANCIAL REVIEW</h2>
  <div class="slide-sub" style="left:22px;top:26px">Do eiusmod tempor incididunt ut labore et dolore magna aliqua.</div>
  <div class="col" style="left:25px;top:43px">
    <div class="col-head"><b>•</b>Sed Ut Perspiciatis</div>
    <div class="col-desc">unde omnis iste natus error sit voluptatem accusantium doloremque laudantium, totam rem aperiam.</div>
    <div class="point" style="margin-top:9px"><div class="point-head">Nemo enim</div><div class="point-desc">Ipsam voluptatem quia voluptas sit aspernatur aut odit<br>aut fugit</div></div>
    <div class="point" style="margin-top:4px"><div class="point-head">Consequuntur</div><div class="point-desc">magni dolores eos qui ratione voluptatem sequi nesciunt.<br>Neque porro quisquam</div></div>
    <div class="point" style="margin-top:4px"><div class="point-head">Adipisci Velit</div><div class="point-desc">sed quia non numquam eius modi tempora incidunt ut labore et dolore magnam aliquam quaerat voluptatem.</div></div>
  </div>
  <div class="col" style="left:158px;top:43px">
    <div class="col-head"><b>•</b>Quis autem vel</div>
    <div class="col-desc">unde omnis iste natus error sit voluptatem accusantium doloremque laudantium, totam rem aperiam, eaque ipsa quae.</div>
    <div class="point" style="margin-top:9px"><div class="point-head">Nemo enim</div><div class="point-desc">Ipsam voluptatem quia voluptas sit aspernatur aut odit<br>aut fugit</div></div>
    <div class="point" style="margin-top:4px"><div class="point-head">Consequuntur</div><div class="point-desc">magni dolores eos qui ratione voluptatem sequi nesciunt.<br>Neque porro quisquam</div></div>
    <div class="point" style="margin-top:4px"><div class="point-head">Adipisci Velit</div><div class="point-desc">sed quia non numquam eius modi tempora incidunt ut labore et dolore magnam aliquam quaerat voluptatem.</div></div>
  </div>
  <div class="wordmark wordmark--dark" style="left:16px;top:142px"><i></i><span>HARBOR LANE<br>GAUGING</span></div>
  <div class="url" style="right:16px;top:145px">harborlanegauging.example</div>
</section>

<!-- Financial review: text -->
<section class="slide slide--light" style="left:452px;top:526px">
  <div class="title-bar" style="left:16px;top:16px;height:9px"></div>
  <h2 class="slide-title" style="left:22px;top:16px;font-size:7.4px">FINANCIAL REVIEW</h2>
  <div class="slide-sub" style="left:22px;top:26px">Do eiusmod tempor incididunt ut labore et dolore magna aliqua.</div>
  <p class="body-copy" style="top:46px">At vero eos et accusamus et iusto odio dignissimos ducimus qui blanditiis praesentium voluptatum deleniti atque corrupti quos dolores et quas molestias excepturi sint occaecati cupiditate non provident, similique sunt in culpa qui officia deserunt mollitia animi, id est laborum et dolorum fuga.</p>
  <p class="body-copy" style="top:69px;width:215px">Et harum quidem rerum facilis est et expedita distinctio. Nam libero tempore, cum soluta nobis est eligendi optio cumque nihil impedit quo minus id quod maxime placeat facere possimus.</p>
  <div class="wordmark wordmark--dark" style="left:16px;top:142px"><i></i><span>HARBOR LANE<br>GAUGING</span></div>
  <div class="url" style="right:16px;top:145px">harborlanegauging.example</div>
</section>

<!-- Thank you -->
<section class="slide slide--dark" style="left:790px;top:527px">
  <div class="wordmark wordmark--light" style="left:0;right:0;top:24px;justify-content:center"><i></i><span>HARBOR LANE<br>GAUGING</span></div>
  <div class="thanks">THANK YOU!</div>
  <div class="thanks-copy">Dicta sunt explicabo. Nemo enim ipsam voluptatem quia voluptas<br>sit aspernatur aut odit aut fugit, sed quia consequuntur magni dolores eos.</div>
  <div class="thanks-rule"></div>
  <div class="url" style="left:0;right:0;top:145px;text-align:center">harborlanegauging.example</div>
</section>

<div class="caption">Brand Fonts - Keystone Sans &amp; Meridia</div>

</body>
</html>
```